Paw Summit Co business card

I need a business card design for a dog training company in Toronto called Paw Summit Co. My training is unique, outdoor training that helps people create a better bond with their dog through communication and understanding their dog's true nature. I do not use treats - but communication and praise for the dog.

I help people create a better life for them and their dog. From puppy training right through to seniors, I offer both group classes called Curbside Poise Course as well as in-home private sessions.

I believe that having a dog is a lifestyle, so I encourage clients to incorporate their dog into their active life. Outdoor activities such as hiking, mental stimulation, proper care and healthy food for their dog are all keys to a healthy and happy dog.

I would like a fresh and modern look that works with my logo. I would like to convey fun, confidence and happiness.

My services are premium services. I am a Certified Dog Trainer, and offer value for money, but my prices are higher than other trainers.
Updates

Thank you to everyone who submitted designs! I'm so impressed with the level of creativity and the options that you all have given me. It will be a difficult choice for sure. As this was my first experience with Art Huddle - it has been a great one.

maren.

Industry/Entity Type

Communication

Requirements
Must have
• Maren Quill, CTE
Certified Trainer Educator
maren@pawsummitco.ca
555-318-0472
pawsummitco.ca

Prefer a double sided card.
Must have Paw Summit Co logo. File attached. I do have a stroke logo for a dark background as well.

Must only use the fonts and colours as outlined in my brand guidelines, which are attached.
Should not have
• no cheesy pet images
do not use the tongue as an element outside of the logo
minimize the use of pink - can be used as an accent colour but should not be a main colour

```html
<!DOCTYPE html>
<html lang="en">
<head>
<meta charset="utf-8">
<title>Paw Summit Co – Business Card</title>
<link rel="stylesheet" href="https://fonts.googleapis.com/css2?family=Short+Stack&display=swap">
<style>
  :root {
    --backdrop: #ebebeb;
    --card-white: #ffffff;
    --brand-green: #8cbf3f;
    --ink-dark: #3f3f42;
    --leather-light: #c4874c;
    --leather-mid: #b3773e;
    --leather-dark: #9a6331;
    --stitch: rgba(255, 240, 220, 0.55);
    --card-shadow: 0 3px 8px rgba(0, 0, 0, 0.35);
  }
  * { margin: 0; padding: 0; box-sizing: border-box; }
  html, body {
    width: 1200px; height: 1086px; overflow: hidden;
    background: var(--backdrop);
    font-family: "Short Stack", "Comic Sans MS", cursive;
  }
  .canvas { position: relative; width: 1200px; height: 1086px; }

  .card {
    position: absolute; width: 873px; height: 500px;
    box-shadow: var(--card-shadow); overflow: hidden;
  }
  .leather {
    position: absolute;
    background:
      radial-gradient(ellipse at 30% 40%, rgba(255,210,160,0.18), transparent 60%),
      radial-gradient(ellipse at 75% 70%, rgba(80,40,10,0.15), transparent 55%),
      linear-gradient(135deg, var(--leather-light), var(--leather-mid) 50%, var(--leather-dark));
  }

  /* Front */
  .card--front { left: 29px; top: 24px; background: var(--card-white); }
  .front-band { left: 0; top: 343px; width: 100%; height: 157px; }
  .front-stitch {
    position: absolute; left: 0; right: 0; top: 19px;
    border-top: 2px dashed var(--stitch);
  }
  .brand-mark {
    position: absolute; display: flex; align-items: center; gap: 12px;
    color: var(--ink-dark); font-weight: 400; white-space: nowrap;
  }
  .brand-mark__dot { border-radius: 50%; background: var(--brand-green); flex: none; }
  .card--front .brand-mark { right: 22px; top: 60px; font-size: 34px; }
  .card--front .brand-mark__dot { width: 24px; height: 24px; }

  .contact { position: absolute; left: 30px; top: 178px; color: var(--ink-dark); }
  .contact__name {
    font-size: 43px; color: var(--brand-green); letter-spacing: 2px;
    line-height: 1; margin-bottom: 14px; font-weight: 400;
  }
  .contact__line { font-size: 24px; line-height: 31px; letter-spacing: 1px; }

  .website {
    position: absolute; left: 0; right: 0; top: 84px; text-align: center;
    font-size: 32px; letter-spacing: 3px; color: var(--brand-green);
  }

  /* Back */
  .card--back { left: 304px; top: 555px; }
  .back-leather { inset: 0; }
  .back-stitch {
    position: absolute; inset: 14px;
    border: 2px dashed var(--stitch);
  }
  .card--back .brand-mark {
    left: 50%; top: 50%; transform: translate(-50%, -50%);
    font-size: 66px; gap: 20px;
  }
  .card--back .brand-mark__dot { width: 44px; height: 44px; }
</style>
</head>
<body>
<main class="canvas">

  <section class="card card--front" aria-label="Card front">
    <div class="brand-mark">
      <span class="brand-mark__dot"></span>
      <span class="brand-mark__name">Paw Summit Co</span>
    </div>

    <div class="contact">
      <h1 class="contact__name">Maren Quill, CTE</h1>
      <p class="contact__line">certified Trainer Educator</p>
      <p class="contact__line">maren@pawsummitco.ca</p>
      <p class="contact__line">555-318-0472</p>
    </div>

    <div class="leather front-band" role="img" aria-label="Stitched brown leather texture band">
      <div class="front-stitch"></div>
      <p class="website">pawsummitco.ca</p>
    </div>
  </section>

  <section class="card card--back" aria-label="Card back">
    <div class="leather back-leather" role="img" aria-label="Brown leather texture background"></div>
    <div class="back-stitch"></div>
    <div class="brand-mark">
      <span class="brand-mark__dot"></span>
      <span class="brand-mark__name">Paw Summit Co</span>
    </div>
  </section>

</main>
</body>
</html>
```